Rise As Captain Book Cover Design

Book Cover Design Brief
Book Title
Rise As Captain
Subtitle
The 10 Quiet Habits of Remarkable Command
Author
Orwen Dalquist
Overview
This book is about leadership that starts within.
Most leadership books focus on tactics or management strategies. This book focuses on the inner disciplines that create powerful leaders — mindset, integrity, focus, empathy, professionalism, honesty, and self-respect.
The tone of the book is bold, direct, confident, and transformational.
This is not a soft or corporate leadership book. It is a call to step up and become the leader you are capable of becoming.
The cover should feel:
• Powerful
• Professional
• Transformational
• Premium
• Memorable
Think best-selling leadership book, not a generic business book.
Target Audience
Business owners
Managers
Entrepreneurs
Team leaders
Professionals who want to grow as leaders
Most readers are ambitious professionals who want to level up their leadership and life.
Design Direction
The design should communicate:
Strength. Discipline. Leadership. Personal transformation.
Avoid cliché leadership visuals like:
• Handshakes
• Office buildings
• Corporate stock imagery
• Teams sitting around tables
The design should feel iconic, bold, and timeless.
Think about covers of successful leadership books such as:
Copper Rituals
Total Stewardship
Won't Break Now
Begin From Purpose
The 36 Rules of Sway
These covers are simple, powerful, and recognizable even at small sizes.
Typography
The title RISE AS CAPTAIN should be:
• Bold
• Strong
• Dominant on the cover
• Easy to read even at small sizes (important for Vellora thumbnails)
The subtitle should be clean and secondary to the title.
The overall typography should feel strong, modern, and premium.
Color Direction
Designers are free to explore colors, but the cover should feel strong and premium, not playful.
Colors that often work well for leadership books include:
Black
Gold
White
Deep blue
Dark red
High contrast and clarity are important.
Style
Preferred style:
• Clean
• Modern
• Minimal
• Strong contrast
Avoid clutter and overly busy designs.
The goal is to create a cover that feels powerful and professional at first glance.
Deliverables
Front cover design for a leadership book.
Final files should include:
• High resolution artwork
• Editable source files
• Print-ready version suitable for publishing
Goal of the Cover
When someone sees this book on Vellora or in a bookstore, they should immediately think:
“This looks like a serious leadership book.”
The design should feel like it belongs next to books by authors such as:
Marcus Thorley
Brandt Osgood
Peter Hollis
Nolan Fairbrook
A strong, confident cover that attracts leaders who want to grow and perform at a higher level.
Target Market(s)
Business Owners and High level managers
Look and feel
Each slider illustrates characteristics of the customer's brand and the style your logo design should communicate.

```html
<!DOCTYPE html>
<html lang="en">
<head>
<meta charset="utf-8">
<title>Rise As Captain — Book Cover</title>
<link rel="stylesheet" href="https://fonts.googleapis.com/css2?family=Playfair+Display:wght@900&family=Open+Sans:wght@400;700&display=swap">
<style>
  :root {
    --stage: #f3f4f4;
    --cover-black: #000000;
    --paper-white: #ffffff;
    --gold-light: #f6d06a;
    --gold-mid: #e4aa35;
    --gold-deep: #c98e1f;
    --figure-light: #f4f4f4;
    --figure-shade: #d8d8d8;
  }
  * { margin: 0; padding: 0; box-sizing: border-box; }
  html, body {
    width: 1200px; height: 900px; overflow: hidden;
    background: var(--stage);
  }
  .stage {
    width: 1200px; height: 900px;
    display: flex; align-items: center; justify-content: center;
  }
  .cover {
    position: relative;
    width: 598px; height: 840px;
    background: var(--cover-black);
    overflow: hidden;
    text-align: center;
  }
  .gold-text {
    background: linear-gradient(100deg, var(--gold-light) 0%, var(--gold-deep) 30%, var(--gold-light) 55%, var(--gold-mid) 75%, var(--gold-light) 100%);
    -webkit-background-clip: text;
    background-clip: text;
    color: transparent;
  }
  .author {
    position: absolute; top: 58px; left: 0; right: 0;
    font-family: "Open Sans", sans-serif;
    font-weight: 700;
    font-size: 23px;
    letter-spacing: 5px;
    text-transform: uppercase;
  }
  .title {
    position: absolute; top: 140px; left: 0; right: 0;
    font-family: "Playfair Display", serif;
    font-weight: 900;
    line-height: 0.92;
  }
  .title-lead { display: block; font-size: 94px; letter-spacing: -1px; }
  .title-main { display: block; font-size: 90px; letter-spacing: -2px; }
  .rule {
    position: absolute; left: 60px; right: 60px; height: 2px;
    background: linear-gradient(90deg, transparent 0%, var(--gold-deep) 20%, var(--gold-light) 50%, var(--gold-deep) 80%, transparent 100%);
  }
  .rule-top { top: 368px; }
  .rule-bottom { top: 452px; }
  .subtitle {
    position: absolute; top: 384px; left: 90px; right: 90px;
    font-family: "Open Sans", sans-serif;
    font-weight: 400;
    font-size: 20px;
    line-height: 1.45;
    color: var(--paper-white);
  }
  .wave {
    position: absolute; left: 0; top: 0; width: 598px; height: 840px;
  }
  .figure-art {
    position: absolute; left: 368px; top: 502px;
    width: 130px; height: 308px;
    border-radius: 46px 46px 8px 8px;
    background: linear-gradient(180deg, var(--figure-light) 0%, var(--figure-shade) 100%);
  }
</style>
</head>
<body>
  <main class="stage">
    <section class="cover">
      <svg class="wave" viewBox="0 0 598 840" aria-hidden="true">
        <path d="M0 828 C70 806 150 758 250 752 C330 748 372 708 402 640 C440 560 500 508 598 472 L598 840 L0 840 Z" fill="var(--paper-white)"/>
      </svg>
      <div class="figure-art" role="img" aria-label="Silhouette of a man in a suit, standing in profile with a hand in his pocket"></div>

      <p class="author gold-text">Orwen Dalquist</p>
      <h1 class="title">
        <span class="title-lead gold-text">Rise As</span>
        <span class="title-main gold-text">CAPTAIN</span>
      </h1>
      <div class="rule rule-top"></div>
      <p class="subtitle">The 10 Quiet Habits of Remarkable Command</p>
      <div class="rule rule-bottom"></div>
    </section>
  </main>
</body>
</html>
```